Life and Personal development life coach needs card design

I need a card design that matches the style and design of my website. I'd like to stay in the same color scheme. Please check out my website for ideas. www.bretamoorvale.com
I have had previous designs for this. I am wondering if you have access to those for more ideas??

```html
<!DOCTYPE html>
<html lang="en">
<head>
<meta charset="utf-8">
<title>Breta Moorvale – Business Cards</title>
<link href="https://fonts.googleapis.com/css2?family=Exo+2:wght@400;500&family=Noto+Serif:wght@400&display=swap" rel="stylesheet">
<style>
  :root {
    --bg: #1c1c1c;
    --lime: #a6d10a;
    --lime-light: #c4e83a;
    --lime-dark: #86aa06;
    --ink: #0c0c0c;
    --ink-soft: #2a2a2a;
    --paper: #d8d8d8;
    --band: #9a9a9a;
    --white: #ffffff;
  }
  * { margin: 0; padding: 0; box-sizing: border-box; }
  html, body { width: 1200px; height: 974px; overflow: hidden; background: var(--bg); }
  body { position: relative; font-family: "Exo 2", sans-serif; }

  .card { position: absolute; width: 540px; height: 310px; box-shadow: 0 10px 30px rgba(0,0,0,.6); }
  .card svg { display: block; width: 100%; height: 100%; }
  .card--contact { left: 40px; top: 180px; }
  .card--name { left: 620px; top: 180px; }

  .name-text { font-family: "Exo 2", sans-serif; font-weight: 400; fill: var(--white); }
  .tagline-text { font-family: "Noto Serif", serif; fill: var(--white); }
  .contact-text { font-family: "Exo 2", sans-serif; fill: var(--ink); }

  .brand-band {
    position: absolute; left: 0; top: 790px; width: 1200px; height: 184px;
    background: var(--band);
  }
  .brand-lockup {
    position: absolute; left: 36px; top: 58px;
    display: flex; align-items: center; gap: 22px;
  }
  .brand-dot { width: 62px; height: 62px; border-radius: 50%; background: var(--lime); }
  .brand-name { font-family: "Exo 2", sans-serif; font-weight: 400; font-size: 52px; color: var(--ink); letter-spacing: 1px; }

  .mini { position: absolute; width: 540px; height: 310px; transform-origin: 0 0; transform: scale(.37); box-shadow: 0 6px 14px rgba(0,0,0,.5); }
  .mini svg { display: block; width: 100%; height: 100%; }
  .mini--contact { left: 765px; top: 42px; }
  .mini--name { left: 968px; top: 46px; transform: scale(.42) rotate(6deg); }
</style>
</head>
<body>

<div class="card card--contact">
  <svg viewBox="0 0 540 310" aria-label="Contact side of business card">
    <rect width="540" height="310" fill="var(--paper)"/>
    <path d="M300 0 H540 V180 C470 150 380 90 300 0 Z" fill="var(--lime)"/>
    <path d="M360 0 H540 V120 C470 100 410 60 360 0 Z" fill="var(--lime-light)" opacity=".55"/>
    <circle cx="480" cy="250" r="185" fill="var(--ink)"/>
    <circle cx="480" cy="250" r="185" fill="none" stroke="rgba(0,0,0,.25)" stroke-width="10"/>
    <circle cx="354" cy="123" r="8" fill="var(--lime)"/>
    <text class="name-text" x="368" y="131" font-size="22">Breta Moorvale</text>
    <text class="tagline-text" x="338" y="152" font-size="9">life and personal development life coach</text>
    <g class="contact-text" font-size="11">
      <rect x="22" y="280" width="9" height="9" rx="2" fill="var(--ink)"/>
      <text x="36" y="289">555-013-4827</text>
      <rect x="120" y="281" width="10" height="7" fill="var(--ink)"/>
      <text x="135" y="289">www.bretamoorvale.com</text>
      <circle cx="318" cy="285" r="4.5" fill="none" stroke="var(--white)" stroke-width="1.3"/>
      <text x="327" y="289" fill="var(--white)">breta@bretamoorvale.com</text>
    </g>
  </svg>
</div>

<div class="card card--name">
  <svg viewBox="0 0 540 310" aria-label="Name side of business card">
    <rect width="540" height="310" fill="var(--ink)"/>
    <path d="M0 0 H540 V30 C380 95 160 95 0 30 Z" fill="var(--lime)"/>
    <path d="M0 0 H540 V14 C380 70 160 70 0 14 Z" fill="var(--lime-light)" opacity=".6"/>
    <path d="M0 310 H540 V280 C380 215 160 215 0 280 Z" fill="var(--lime)"/>
    <path d="M0 310 H540 V296 C380 240 160 240 0 296 Z" fill="var(--lime-light)" opacity=".6"/>
    <circle cx="270" cy="130" r="14" fill="var(--lime)"/>
    <text class="name-text" x="270" y="192" font-size="36" text-anchor="middle">Breta Moorvale</text>
  </svg>
</div>

<section class="brand-band">
  <div class="brand-lockup">
    <span class="brand-dot"></span>
    <span class="brand-name">Breta Moorvale</span>
  </div>

  <div class="mini mini--contact">
    <svg viewBox="0 0 540 310" aria-hidden="true">
      <rect width="540" height="310" fill="var(--paper)"/>
      <path d="M300 0 H540 V180 C470 150 380 90 300 0 Z" fill="var(--lime)"/>
      <circle cx="480" cy="250" r="185" fill="var(--ink)"/>
      <circle cx="354" cy="123" r="8" fill="var(--lime)"/>
      <text class="name-text" x="368" y="131" font-size="22">Breta Moorvale</text>
      <text class="tagline-text" x="338" y="152" font-size="9">life and personal development life coach</text>
      <g class="contact-text" font-size="11">
        <text x="22" y="289">555-013-4827</text>
        <text x="135" y="289">www.bretamoorvale.com</text>
        <text x="327" y="289" fill="var(--white)">breta@bretamoorvale.com</text>
      </g>
    </svg>
  </div>

  <div class="mini mini--name">
    <svg viewBox="0 0 540 310" aria-hidden="true">
      <rect width="540" height="310" fill="var(--ink)"/>
      <path d="M0 0 H540 V30 C380 95 160 95 0 30 Z" fill="var(--lime)"/>
      <path d="M0 310 H540 V280 C380 215 160 215 0 280 Z" fill="var(--lime)"/>
      <circle cx="270" cy="130" r="14" fill="var(--lime)"/>
      <text class="name-text" x="270" y="192" font-size="36" text-anchor="middle">Breta Moorvale</text>
    </svg>
  </div>
</section>

</body>
</html>
```